I own a small business whose primary function is Professional Fashion and Commercial Photography and has a secondary function of Talent Management of Models/Actors. I've used NorthPress in the past to print my own design, but I'd like something a bit more topical, fresh and done by an artist instead of a photographer (me).

My company logo is included with a few selected horizontal (landscape) photos of some of my models--I'd like to use a single model photo as the background for the entire card, either in color or converted to black and white, at opacity enough to see the photo but not too much to obscure any text or the company logo, or use a photo as a share of the card (not the entire background), or use all the three models on the card in some manor... Our company colors are white, black, grey-silver and red.

Industry/Entity Type

Small Business

Contact Information for Business Card

Daniel Hartwell, Owner
KTL Productions
PO Box 7713
Brattleboro VT 05917-7713
(555) 010-0147
dan@ktlproductions-example,.com

```html
<!DOCTYPE html>
<html lang="en">
<head>
<meta charset="utf-8">
<title>KTL Productions – Business Card</title>
<link rel="stylesheet" href="https://fonts.googleapis.com/css2?family=Lato:wght@400;700;900&display=swap">
<style>
  :root {
    --bg: #e4e4e6;
    --white: #ffffff;
    --ink: #111111;
    --grey: #6d6d6d;
    --silver: #ececec;
    --rule: #c9c9c9;
    --red: #d81f26;
    --photo-blue-a: #5d7d92;
    --photo-blue-b: #9fb6c4;
    --photo-dark-a: #2a2a2e;
    --photo-dark-b: #6b5a4c;
    --photo-red-a: #b3121c;
    --photo-red-b: #d8323a;
  }
  * { box-sizing: border-box; margin: 0; padding: 0; }
  html, body { width: 1200px; height: 926px; overflow: hidden; }
  body {
    background: var(--bg);
    font-family: "Lato", Arial, sans-serif;
    display: flex;
    flex-direction: column;
    align-items: center;
    justify-content: center;
    gap: 36px;
  }
  .card {
    position: relative;
    width: 735px;
    height: 420px;
    background: var(--white);
    overflow: hidden;
    box-shadow: 0 6px 18px rgba(0,0,0,.18);
  }
  .photo-strip { position: absolute; left: 0; top: 0; width: 100%; display: flex; }
  .photo { height: 100%; }
  .photo--blue { width: 30%; background: linear-gradient(160deg, var(--photo-blue-b), var(--photo-blue-a)); }
  .photo--dark { width: 40%; background: linear-gradient(180deg, var(--photo-dark-a) 0%, var(--photo-dark-b) 55%, var(--photo-dark-a) 100%); }
  .photo--red  { width: 30%; background: linear-gradient(160deg, var(--photo-red-b), var(--photo-red-a)); }

  /* Front */
  .card--front .photo-strip { height: 100%; }
  .brand-band {
    position: absolute; left: 0; right: 0; top: 150px; height: 112px;
    background: rgba(255,255,255,.82);
    display: flex; align-items: center; justify-content: center;
  }
  .brand { display: flex; align-items: center; gap: 14px; }
  .brand__mark { width: 26px; height: 26px; background: var(--red); }
  .brand__name {
    font-weight: 700; font-size: 40px; letter-spacing: 4px; color: var(--ink);
    border-bottom: 2px solid var(--red); padding-bottom: 4px;
  }

  /* Back */
  .card--back .photo-strip { height: 218px; }
  .identity { position: absolute; top: 236px; left: 0; right: 0; text-align: center; }
  .identity__rule { position: absolute; left: 80px; right: 80px; top: -4px; border-top: 1px solid var(--rule); }
  .identity__name { font-size: 30px; font-weight: 400; color: var(--red); text-transform: uppercase; letter-spacing: .5px; line-height: 1.15; }
  .identity__name b { font-weight: 900; }
  .identity__role { font-size: 21px; font-weight: 700; color: var(--ink); line-height: 1.1; }
  .contacts {
    position: absolute; top: 298px; left: 60px; right: 60px;
    display: flex; justify-content: space-between; align-items: flex-start;
    color: var(--grey); font-size: 18px; letter-spacing: .5px; line-height: 1.1;
  }
  .contact { display: flex; flex-direction: column; align-items: center; gap: 3px; }
  .contact svg { width: 18px; height: 18px; fill: var(--ink); }
  .contact--email { margin-top: 14px; }
  .contact--mobile { margin-top: 28px; }
  .address-bar {
    position: absolute; left: 0; right: 0; bottom: 0; height: 38px;
    background: var(--silver);
    display: flex; align-items: center; justify-content: center;
    color: var(--grey); font-size: 18px; letter-spacing: 2px; word-spacing: 3px;
  }
</style>
</head>
<body>

  <section class="card card--front" aria-label="Business card front">
    <div class="photo-strip">
      <div class="photo photo--blue" role="img" aria-label="Portrait of a blond model in a plaid shirt"></div>
      <div class="photo photo--dark" role="img" aria-label="Close portrait of a model in a dark cap"></div>
      <div class="photo photo--red" role="img" aria-label="Portrait of a model in a red shirt on red backdrop"></div>
    </div>
    <div class="brand-band">
      <div class="brand">
        <span class="brand__mark"></span>
        <span class="brand__name">KTL Productions</span>
      </div>
    </div>
  </section>

  <section class="card card--back" aria-label="Business card back">
    <div class="photo-strip">
      <div class="photo photo--blue" role="img" aria-label="Portrait of a blond model in a plaid shirt"></div>
      <div class="photo photo--dark" role="img" aria-label="Close portrait of a model in a dark cap"></div>
      <div class="photo photo--red" role="img" aria-label="Portrait of a model in a red shirt on red backdrop"></div>
    </div>

    <div class="identity">
      <div class="identity__rule"></div>
      <h1 class="identity__name"><b>Daniel</b> Hartwell</h1>
      <p class="identity__role">owner</p>
    </div>

    <div class="contacts">
      <div class="contact contact--phone">
        <svg viewBox="0 0 24 24" aria-hidden="true"><path d="M6.6 10.8a15 15 0 0 0 6.6 6.6l2.2-2.2c.3-.3.7-.4 1-.2 1.1.4 2.3.6 3.6.6.6 0 1 .4 1 1V20c0 .6-.4 1-1 1A17 17 0 0 1 3 4c0-.6.4-1 1-1h3.5c.6 0 1 .4 1 1 0 1.3.2 2.5.6 3.6.1.3 0 .7-.2 1z"/></svg>
        <span>05917-7713</span>
      </div>
      <div class="contact contact--email">
        <svg viewBox="0 0 24 24" aria-hidden="true"><path d="M2 5h20v14H2z M4 7v.4l8 5.2 8-5.2V7z" fill-rule="evenodd"/></svg>
        <span>dan@ktlproductions-example.com</span>
      </div>
      <div class="contact contact--mobile">
        <svg viewBox="0 0 24 24" aria-hidden="true"><path d="M7 2h10a1 1 0 0 1 1 1v18a1 1 0 0 1-1 1H7a1 1 0 0 1-1-1V3a1 1 0 0 1 1-1zm1 3v12h8V5z"/></svg>
        <span>(555) 010-0147</span>
      </div>
    </div>

    <footer class="address-bar">KTL Productions&nbsp; PO Box 7713 Cedar Hollow</footer>
  </section>

</body>
</html>
```